Electronic Time-sheet for phones

I need a time-sheet that can be accessed on the phone, be completed, then have the ability to electronically sign. The time sheet needs to be used two fold for supervision to verify hours and quantities and also for the client to be able to electronically sign. The time-sheet should be daily or weekly if we can get the data to fit. We are trying to streamline field supervisors having to log on to a computer to access a server just to do time-sheets. We need it to be user friendly. We need to have two places to have electronic signatures. One for supervisor or authorized representative and the other for the client to sign.

Target Market(s)

Industrial clients

Industry/Entity Type

Oil And Gas

Requirements
Must have
• hours, quantities, project name, location, signature line etc
Nice to have
• n/a
Should not have
• n/a

```html
<!DOCTYPE html>
<html lang="en">
<head>
<meta charset="utf-8">
<title>Field Timesheet – Mobile Screens</title>
<link href="https://fonts.googleapis.com/css2?family=Libre+Baskerville:wght@400;700&family=Roboto+Condensed:wght@400;700&family=Open+Sans:wght@400;600&display=swap" rel="stylesheet">
<style>
:root{
  --stage:#8a8a8a;
  --blue:#3a52a3;
  --navy:#1d2c52;
  --ink:#1b1b1b;
  --label:#6d6d6d;
  --line:#e3e3e3;
  --field:#bdbdbd;
  --tint:#f2f2f2;
  --white:#ffffff;
}
*{box-sizing:border-box;margin:0;padding:0}
html,body{width:1066px;height:1200px;overflow:hidden;background:var(--stage)}
.stage{position:relative;width:1333px;height:1500px;transform:scale(.8);transform-origin:0 0;font-family:"Open Sans",sans-serif;color:var(--ink)}
.caption{position:absolute;font-family:"Libre Baskerville",serif;color:var(--white);font-size:17px;text-align:center}
.caption small{font-size:12px;letter-spacing:.5px}
.caption .sub{display:block;font-size:14px;margin-top:6px}
.screen{position:absolute;width:375px;background:var(--white);border-radius:40px;overflow:hidden}
.abs{position:absolute}
.bar{position:absolute;left:0;top:0;width:100%;height:88px;background:var(--blue);color:var(--white)}
.time{position:absolute;left:31px;top:19px;font-size:10px;font-family:"Roboto Condensed",sans-serif;opacity:.85}
.bar-title{position:absolute;top:57px;width:100%;text-align:center;font-family:"Roboto Condensed",sans-serif;font-size:16px}
.cancel{position:absolute;right:16px;top:60px;font-family:"Roboto Condensed",sans-serif;font-size:11px;display:flex;align-items:center;gap:6px}
.brand{position:absolute;left:0;width:100%;text-align:center;font-family:"Roboto Condensed",sans-serif;font-weight:700;font-size:50px;color:var(--navy);letter-spacing:1px;line-height:1}
.label{position:absolute;left:16px;font-family:"Roboto Condensed",sans-serif;font-size:12px;color:var(--label);letter-spacing:.3px}
.input{position:absolute;left:16px;width:343px;height:44px;border:1px solid var(--field);background:var(--white);font-size:15px;padding:0 8px;display:flex;align-items:center}
.table{position:absolute;left:0;width:100%;font-family:"Roboto Condensed",sans-serif;font-size:12px}
.row{display:grid;grid-template-columns:175px 76px 40px 48px;padding-left:16px;height:35px;align-items:center;border-bottom:1px solid var(--line)}
.row>span:nth-child(3),.row>span:nth-child(4){text-align:center}
.row.head{height:22px;color:var(--label);font-size:10px;border-bottom:1px solid var(--line)}
.row.total{background:var(--tint);border-bottom:none;font-weight:700;font-size:13px}
.name b{font-weight:400;font-size:13px}
.name small{font-size:10px}
.s1 .name{color:var(--blue)}
.pill{position:absolute;left:16px;height:28px;border:1px solid var(--blue);border-radius:14px;color:var(--blue);font-family:"Roboto Condensed",sans-serif;font-weight:700;font-size:11px;display:flex;align-items:center;justify-content:center;gap:5px}
.cta{position:absolute;left:68px;width:240px;height:48px;background:var(--blue);color:var(--white);border-radius:4px;font-family:"Roboto Condensed",sans-serif;font-weight:700;font-size:16px;display:flex;align-items:center;justify-content:center;gap:9px}
.comment-box{position:absolute;left:16px;width:343px;border:1px solid var(--field);padding:12px 8px;font-size:13px;line-height:22px}
.band{position:absolute;left:0;width:100%;background:#f5f5f5}
.cell{position:absolute;height:44px;border:1px solid var(--field);background:var(--white);font-size:15px;padding:0 8px;display:flex;align-items:center}
.trash{position:absolute;left:346px}
.info{position:absolute;left:16px;display:flex;gap:8px;align-items:center}
.info .ic{width:40px;height:40px;border-radius:50%;background:var(--blue);display:flex;align-items:center;justify-content:center}
.info .k{font-family:"Roboto Condensed",sans-serif;font-size:10px;color:var(--label)}
.info .v{font-size:15px}
.info .v small{font-size:11px}
.sign{position:absolute;left:16px;width:343px;height:56px;border:1px solid var(--field)}
.sign.supervisor{border-left:5px solid #cfcfcf}
.sign.client{border:1px solid var(--blue);border-left:5px solid var(--blue)}
.sig-ink{position:absolute;left:22px;top:10px;width:130px;height:36px;background:#eceef4;border-radius:4px}
.sig-date{position:absolute;right:10px;top:10px;height:34px;border-left:1px solid var(--line);padding-left:10px;font-family:"Roboto Condensed",sans-serif;font-size:11px;text-align:center;line-height:13px}
.sig-date small{font-size:9px}
.comment-text{position:absolute;left:16px;width:343px;font-size:12.4px;line-height:22px;color:#333}
.home{position:absolute;left:121px;width:134px;height:4px;border-radius:2px;background:#efefef}
</style>
</head>
<body>
<div class="stage">

  <div class="caption" style="left:58px;top:47px;width:375px"><small>STEP 1:</small> Supervisor creates a timesheet</div>
  <div class="caption" style="left:479px;top:557px;width:390px">Add an employee screen<span class="sub">(click on “Add Employee” button)</span></div>
  <div class="caption" style="left:900px;top:47px;width:390px"><small>STEP 2:</small> Supervisor &amp; Client review and sign</div>

  <!-- Create timesheet -->
  <section class="screen s1" style="left:58px;top:97px;height:1344px">
    <div class="bar"><span class="time">5:30</span><div class="bar-title">CREATE TIMESHEET</div></div>
    <div class="brand" style="top:128px">VOLTA</div>

    <div class="label" style="top:198px">PROJECT NAME</div>
    <div class="input" style="top:218px">Project Name</div>
    <div class="label" style="top:284px">PROJECT #</div>
    <div class="input" style="top:304px">88999</div>
    <div class="label" style="top:370px">CLIENT</div>
    <div class="input" style="top:390px">Northfield Chemical, Inc.</div>
    <div class="label" style="top:456px">LOCATION</div>
    <div class="input" style="top:476px">New Unit#1</div>
    <div class="label" style="top:542px">DATE</div>
    <div class="input" style="top:562px;justify-content:space-between">November 6, 2018
      <svg width="16" height="16" viewBox="0 0 16 16" fill="none" stroke="#9a9a9a" stroke-width="1.2"><rect x="1.5" y="2.5" width="13" height="12" rx="1"/><path d="M1.5 6h13M5 1v3M11 1v3M5 9h1M8 9h1M11 9h1M5 12h1M8 12h1"/></svg>
    </div>

    <div class="table" style="top:640px">
      <div class="row head"><span></span><span>PHASE CODE</span><span>HOUR</span><span>QTY.</span></div>
      <div class="row"><span class="name"><b>John Doe</b> <small>(FOR)</small></span><span>17994</span><span>2</span><span>0</span></div>
      <div class="row"><span></span><span>16136-210</span><span>4</span><span>0</span></div>
      <div class="row"><span></span><span>16137-210</span><span>4</span><span>0</span></div>
      <div class="row"><span class="name"><b>Jason Doe</b> <small>(App-A)</small></span><span>17994</span><span>5</span><span>0</span></div>
      <div class="row"><span></span><span>16136-210</span><span>5</span><span>12</span></div>
      <div class="row"><span class="name"><b>Jack Doe</b> <small>(JE - A)</small></span><span>17994</span><span>5</span><span>25</span></div>
      <div class="row"><span></span><span>16137-210</span><span>5</span><span>12</span></div>
      <div class="row total"><span></span><span>TOTAL</span><span>30</span><span>49</span></div>
    </div>

    <div class="pill" style="top:959px;width:126px"><svg width="10" height="10" viewBox="0 0 10 10" stroke="#3a52a3" stroke-width="1.8"><path d="M5 0v10M0 5h10"/></svg>ADD EMPLOYEE</div>

    <div class="label" style="top:1025px">COMMENT</div>
    <div class="comment-box" style="top:1045px;height:158px">Lorem ipsum dolor sit amet, consectetur adipiscing elit. Suspendisse sollicitudin odio aliquet urna viverra, sit amet vehicula magna varius. Sed turpis metus, semper eu accumsan in, elementum non enim. Vestibulum ante ipsum primisy in faucibus orci luctus et ultrices posuere cubilia.</div>

    <div class="cta" style="top:1243px"><svg width="15" height="14" viewBox="0 0 15 14" fill="#fff"><path d="M0 0l15 7-15 7 3-7z"/></svg>CREATE</div>
    <div class="home" style="top:1330px"></div>
  </section>

  <!-- Employee -->
  <section class="screen" style="left:479px;top:630px;height:811px">
    <div class="bar"><span class="time">5:30</span><div class="bar-title">EMPLOYEE</div>
      <div class="cancel"><svg width="10" height="10" viewBox="0 0 10 10" stroke="#fff" stroke-width="1.3"><path d="M0 0l10 10M10 0L0 10"/></svg>CANCEL</div></div>

    <div class="label" style="top:126px">EMPLOYEE NAME</div>
    <div class="input" style="top:146px">John Doe</div>
    <div class="label" style="top:212px">CLASS</div>
    <div class="label" style="top:212px;left:191px">EMPLOYEE #</div>
    <div class="input" style="top:232px;width:167px">FOR</div>
    <div class="input" style="top:232px;left:191px;width:167px">1254</div>

    <div class="band" style="top:315px;height:251px"></div>
    <div class="label" style="top:338px">PHASE CODE</div>
    <div class="label" style="top:338px;left:205px">HOUR</div>
    <div class="label" style="top:338px;left:281px">QTY.</div>

    <div class="cell" style="top:358px;left:16px;width:172px">17994</div>
    <div class="cell" style="top:358px;left:187px;width:72px">2</div>
    <div class="cell" style="top:358px;left:258px;width:73px">0</div>
    <div class="cell" style="top:410px;left:16px;width:172px">16136-210</div>
    <div class="cell" style="top:410px;left:187px;width:72px">4</div>
    <div class="cell" style="top:410px;left:258px;width:73px">0</div>
    <div class="cell" style="top:462px;left:16px;width:172px">16137-210</div>
    <div class="cell" style="top:462px;left:187px;width:72px">4</div>
    <div class="cell" style="top:462px;left:258px;width:73px">0</div>
    <svg class="trash" style="top:372px" width="12" height="14" viewBox="0 0 12 14" fill="#c4c4c4"><path d="M0 2h12v1.5H0zM4 0h4v2H4zM1.5 4h9l-.8 10H2.3z"/></svg>
    <svg class="trash" style="top:424px" width="12" height="14" viewBox="0 0 12 14" fill="#c4c4c4"><path d="M0 2h12v1.5H0zM4 0h4v2H4zM1.5 4h9l-.8 10H2.3z"/></svg>
    <svg class="trash" style="top:476px" width="12" height="14" viewBox="0 0 12 14" fill="#c4c4c4"><path d="M0 2h12v1.5H0zM4 0h4v2H4zM1.5 4h9l-.8 10H2.3z"/></svg>

    <div class="pill" style="top:514px;width:106px;background:var(--white)"><svg width="10" height="10" viewBox="0 0 10 10" stroke="#3a52a3" stroke-width="1.8"><path d="M5 0v10M0 5h10"/></svg>ADD PHASE</div>

    <div class="cta" style="top:606px"><svg width="15" height="14" viewBox="0 0 15 14" fill="#fff"><path d="M0 0l15 7-15 7 3-7z"/></svg>SAVE</div>
    <div class="abs" style="top:678px;width:100%;text-align:center;font-family:'Roboto Condensed',sans-serif;font-size:12px;color:#9a9a9a">
      <svg width="10" height="12" viewBox="0 0 12 14" fill="#b0b0b0"><path d="M0 2h12v1.5H0zM4 0h4v2H4zM1.5 4h9l-.8 10H2.3z"/></svg> DELETE EMPLOYEE</div>
    <div class="home" style="top:798px"></div>
  </section>

  <!-- Review and sign -->
  <section class="screen" style="left:900px;top:97px;height:1250px">
    <span class="time" style="color:#b0b0b0">5:30</span>
    <div class="abs" style="left:16px;top:59px;font-family:'Roboto Condensed',sans-serif;font-size:11px;color:var(--blue)">‹ BACK</div>
    <div class="brand" style="top:88px">VOLTA</div>
    <div class="abs" style="top:154px;left:0;width:100%;height:1px;background:var(--line)"></div>
    <div class="abs" style="top:145px;left:130px;width:115px;text-align:center;background:var(--white);font-family:'Roboto Condensed',sans-serif;font-weight:700;font-size:14px;color:#b5b5b5;letter-spacing:.5px">TIMESHEET</div>

    <div class="info" style="top:192px"><div class="ic"><svg width="14" height="20" viewBox="0 0 14 20" fill="#fff"><path d="M9 0L1 11h5l-2 9 9-12H8z"/></svg></div><div><div class="k">PROJECT NAME</div><div class="v">Project Name <small>(88999)</small></div></div></div>
    <div class="info" style="top:248px"><div class="ic"><svg width="16" height="16" viewBox="0 0 16 16" fill="#fff"><circle cx="8" cy="4.5" r="3.5"/><path d="M1 16c0-4 3-6.5 7-6.5s7 2.5 7 6.5z"/></svg></div><div><div class="k">PREPARED FOR</div><div class="v">Northfield Chemical, Inc.</div></div></div>
    <div class="info" style="top:304px"><div class="ic"><svg width="14" height="20" viewBox="0 0 14 20" fill="#fff"><path d="M7 0a7 7 0 017 7c0 5-7 13-7 13S0 12 0 7a7 7 0 017-7zm0 4a3 3 0 100 6 3 3 0 000-6z"/></svg></div><div><div class="k">LOCATION</div><div class="v">New Unit#1</div></div></div>
    <div class="info" style="top:360px"><div class="ic"><svg width="16" height="16" viewBox="0 0 16 16" fill="none" stroke="#fff" stroke-width="1.5"><rect x="1.5" y="2.5" width="13" height="12" rx="1"/><path d="M1.5 6h13M5 1v3M11 1v3M5 9h1M8 9h1M11 9h1M5 12h1M8 12h1"/></svg></div><div><div class="k">DATE</div><div class="v">November 6, 2018</div></div></div>

    <div class="table" style="top:434px">
      <div class="row head"><span></span><span>PHASE CODE</span><span>HOUR</span><span>QTY.</span></div>
      <div class="row"><span class="name"><b>John Doe</b> <small>(FOR)</small></span><span>17994</span><span>2</span><span>0</span></div>
      <div class="row"><span></span><span>16136-210</span><span>4</span><span>0</span></div>
      <div class="row"><span></span><span>16137-210</span><span>4</span><span>0</span></div>
      <div class="row"><span class="name"><b>Jason Doe</b> <small>(App-A)</small></span><span>17994</span><span>5</span><span>0</span></div>
      <div class="row"><span></span><span>16136-210</span><span>5</span><span>12</span></div>
      <div class="row"><span class="name"><b>Jack Doe</b> <small>(JE - A)</small></span><span>17994</span><span>5</span><span>25</span></div>
      <div class="row"><span></span><span>16137-210</span><span>5</span><span>12</span></div>
      <div class="row total"><span></span><span>TOTAL</span><span>30</span><span>49</span></div>
    </div>

    <div class="label" style="top:775px;font-size:13px;font-weight:700">COMMENT:</div>
    <div class="comment-text" style="top:794px">Lorem ipsum dolor sit amet, consectetur adipiscing elit. Suspendisse sollicitudin odio aliquet urna viverra, sit amet vehicula magna varius. Sed turpis metus, semper eu accumsan in, elementum non enim. Vestibulum ante ipsum primisy in faucibus orci luctus et ultrices posuere cubilia.</div>

    <div class="label" style="top:939px;font-size:10px">SUPERVISOR / AUTHORIZED REPRESENTATIVE</div>
    <div class="sign supervisor" style="top:957px">
      <div class="sig-ink" role="img" aria-label="Handwritten supervisor signature of John Doe"></div>
      <div class="sig-date">NOV. 8<br><small>2018</small></div>
    </div>
    <div class="label" style="top:1035px;font-size:10px;color:var(--blue)">CLIENT</div>
    <div class="sign client" style="top:1053px"></div>

    <div class="cta" style="top:1149px"><svg width="15" height="14" viewBox="0 0 15 14" fill="#fff"><path d="M0 0l15 7-15 7 3-7z"/></svg>SUBMIT</div>
    <div class="home" style="top:1237px"></div>
  </section>

</div>
</body>
</html>
```